VERIDAX Need a luxury modern business card designed.

Need a luxury modern business card designed. refer to the uploaded files for the company name and logo in the zip file under source files. i will making my descion on monday. so please send in before then so if we need to edit we will have the time. we have a trade show coming up and im on a deadline for printer.

Target Market(s)

high end clients

Contact Information for Business Card

Company nAme and logo. Calvin Ostrow Co-Founder / Project Manager Office # 416-555-0193 Cell # 416-555-0147 VERIDAX.CA Calvin@veridax.ca

Font styles to use
Other font styles liked:
• Modern

Requirements
Must have
• Company name and logo, contact info, using the black, gold and white color scheme.

```html
<!DOCTYPE html>
<html lang="en">
<head>
<meta charset="utf-8">
<title>VERIDAX Business Card</title>
<link rel="stylesheet" href="https://fonts.googleapis.com/css2?family=Comfortaa:wght@700&family=Montserrat:wght@300;400&display=swap">
<style>
  :root {
    --charcoal: #383435;
    --gold: #e9c23a;
    --olive-gold: #948a4e;
    --white: #ffffff;
    --ink: #2f2b2c;
    --page: #ffffff;
  }
  * { margin: 0; padding: 0; box-sizing: border-box; }
  html, body {
    width: 1200px; height: 1200px; overflow: hidden;
    background: var(--page);
  }
  .sheet { position: relative; width: 1200px; height: 1200px; }

  .card {
    position: absolute; left: 219px; width: 762px; height: 456px;
    overflow: hidden;
  }

  .brand-mark {
    position: absolute; left: 50%; transform: translateX(-50%);
    background: var(--olive-gold);
  }
  .brand-name {
    position: absolute; left: 0; right: 0; text-align: center;
    font-family: "Montserrat", sans-serif; font-weight: 300;
    line-height: 1; letter-spacing: 0.28em; text-indent: 0.28em;
  }

  /* Front */
  .card-front {
    top: 117px; background: var(--charcoal);
    border-left: 6px solid var(--gold);
    border-bottom: 6px solid var(--gold);
  }
  .card-front .brand-mark { top: 140px; width: 62px; height: 62px; }
  .card-front .brand-name { top: 256px; font-size: 56px; color: var(--white); }
  .website {
    position: absolute; left: 0; right: 0; top: 395px; text-align: center;
    font-family: "Montserrat", sans-serif; font-weight: 400;
    font-size: 17px; color: var(--white); letter-spacing: 0.02em;
  }

  /* Back */
  .card-back {
    top: 627px; background: var(--white);
    border: 1px solid var(--ink);
  }
  .back-swoosh { position: absolute; inset: 0; }
  .card-back .brand-mark { top: 52px; width: 52px; height: 52px; }
  .card-back .brand-name { top: 148px; font-size: 42px; color: var(--ink); }
  .person-name {
    position: absolute; left: 0; right: 0; top: 214px; text-align: center;
    font-family: "Comfortaa", sans-serif; font-weight: 700;
    font-size: 29px; color: var(--gold);
  }
  .person-role {
    position: absolute; left: 0; right: 0; top: 256px; text-align: center;
    font-family: "Comfortaa", sans-serif; font-weight: 700;
    font-size: 19px; color: var(--ink);
  }
  .contact-row {
    position: absolute; top: 388px; left: 0; right: 0; height: 24px;
    font-family: "Comfortaa", sans-serif; font-weight: 700;
    font-size: 15.5px; color: var(--white);
  }
  .contact-item {
    position: absolute; display: flex; align-items: center; gap: 9px; top: 0;
  }
  .contact-item svg { width: 15px; height: 15px; fill: var(--gold); }
  .contact-office { left: 58px; }
  .contact-cell { left: 310px; }
  .contact-email { left: 502px; }
</style>
</head>
<body>
<main class="sheet">

  <section class="card card-front" aria-label="Business card front">
    <div class="brand-mark" role="img" aria-label="Company logo symbol"></div>
    <div class="brand-name">VERIDAX</div>
    <p class="website">WWW.VERIDAX.CA</p>
  </section>

  <section class="card card-back" aria-label="Business card back">
    <svg class="back-swoosh" viewBox="0 0 760 454" preserveAspectRatio="none" aria-hidden="true">
      <defs>
        <linearGradient id="goldSweep" x1="0" x2="1" y1="0" y2="0">
          <stop offset="0" stop-color="#e9c23a"/>
          <stop offset="0.2" stop-color="#f1d774"/>
          <stop offset="0.34" stop-color="#ffffff"/>
          <stop offset="0.5" stop-color="#ecc43c"/>
          <stop offset="0.66" stop-color="#ffffff"/>
          <stop offset="0.8" stop-color="#f1d774"/>
          <stop offset="1" stop-color="#e9c23a"/>
        </linearGradient>
      </defs>
      <path d="M0,284 Q380,364 760,284 L760,454 L0,454 Z" fill="url(#goldSweep)"/>
      <path d="M0,301 Q380,381 760,301 L760,454 L0,454 Z" fill="#383435"/>
    </svg>

    <div class="brand-mark" role="img" aria-label="Company logo symbol"></div>
    <div class="brand-name">VERIDAX</div>
    <h1 class="person-name">Calvin Ostrow</h1>
    <p class="person-role">Project Manager</p>

    <div class="contact-row">
      <div class="contact-item contact-office">
        <svg viewBox="0 0 24 24" aria-hidden="true"><path d="M6.6 10.8a15.1 15.1 0 0 0 6.6 6.6l2.2-2.2c.3-.3.7-.4 1-.2 1.1.4 2.3.6 3.6.6.6 0 1 .4 1 1V20c0 .6-.4 1-1 1A17 17 0 0 1 3 4c0-.6.4-1 1-1h3.5c.6 0 1 .4 1 1 0 1.3.2 2.5.6 3.6.1.3 0 .7-.2 1z"/></svg>
        <span>416-555-0193</span>
      </div>
      <div class="contact-item contact-cell">
        <svg viewBox="0 0 24 24" aria-hidden="true"><path d="M8 1h8a2 2 0 0 1 2 2v18a2 2 0 0 1-2 2H8a2 2 0 0 1-2-2V3a2 2 0 0 1 2-2zm0 3v14h8V4zm4 15.5a1 1 0 1 0 0 2 1 1 0 0 0 0-2z"/></svg>
        <span>416-555-0147</span>
      </div>
      <div class="contact-item contact-email">
        <svg viewBox="0 0 24 24" aria-hidden="true"><path d="M2 5h20v14H2zm2 2v.4l8 5.6 8-5.6V7zm0 2.8V17h16V9.8l-8 5.6z"/></svg>
        <span>Calvin@veridax.ca</span>
      </div>
    </div>
  </section>

</main>
</body>
</html>
```